Buch-/E-Book-Cover Ratgeber Selbstliebe
Zielgruppe
Ich suche ein ansprechendes Cover-Design für mein E-Book. Es handelt sich um einen Ratgeber über Selbstliebe und meine Zielgruppe sind Frauen im Alter zwischen 18 und 40 Jahren.
Aufgabenstellung
Klare Designs, die das Thema des Ratgebers unterstreichen und nicht durch unnötige Details und unlesbare Verschnörkelungen ablenken. Die weibliche Zielgruppe sollte vor allem angesprochen werden, dies sollte auch in der Farbauswahl berücksichtigt werden. Das bedeutet helle Farbtöne wie rosa, rot, hellblau oder pastellgelb.
Die Umsetzung des Motivs überlasse ich der Kreativität des Designers. Es können sowohl Stockfotos von einer jungen Frau gewählt werden, die Freude ausstrahlt und sich wohl in ihrer Haut fühlt (wo vielleicht auch warmes Licht oder Sonnenschein auf dem Cover zu sehen sind) oder ein rein graphisches Bild aus zusammengesetzten Elementen, die eine junge Frau zeigen und ihre Beziehung zur Selbstliebe deutlich wird. Es muss nicht zwangsläufig ein Herz abgebildet werden, nur weil es das erste ist, was man vielleicht mit Liebe assoziiert, auch wenn ein kreativer Umgang mit dem Herz als Symbol eine durchaus ansprechende Wirkung haben kann. Wichtig wäre mir eine kreative Umsetzung im Bild, wodurch das Thema der 'Selbstliebe' sofort deutlich wird und den Käufer anspricht. Der Titel sollte genauso deutlich hervorstechen wie das zentrale Motiv. Außerdem sollte gleich erkennbar sein, dass es sich nicht um einen Roman, sondern um einen Ratgeber handelt. Daher bin ich an einer graphischen Aufbereitung genauso wie an einem Fotomotiv interessiert. Bereits existierende Cover zu einem ähnlichen Ratgeber- Thema, die ich ansprechend finde, füge ich im Anhang hinzu.
Bitte nicht die im Anhang eingefügten Dateien verwenden, da sie urheberrechtlich geschützt sind! Sie dienen nur als Interpretationsvorschlag.
Titel: Innere Ruhe finden
Untertitel: Wie aus kleinen Gewohnheiten jeden Tag neue Gelassenheit im Alltag wächst
Autorenname: Jana Roth
Der Buchrücken soll farblich an das Cover angepasst werden. Der Buchrückentext folgt noch im Anhang.
Das E-Book wird es auch als Paperback Buch geben. Der Umfang des Ra..

```html
<!DOCTYPE html>
<html lang="de">
<head>
<meta charset="UTF-8">
<title>Innere Ruhe finden – Jana Roth</title>
<link rel="stylesheet" href="https://fonts.googleapis.com/css2?family=Gochi+Hand&family=Spectral:wght@500;600&display=swap">
<style>
  :root {
    --page-bg: #e4e4e4;
    --cover-pink: #f7b9ca;
    --cover-pink-deep: #f2a3b8;
    --accent-red: #e30613;
    --title-white: #fbfaf7;
    --subtitle-white: #ffffff;
    --photo-warm: #e9c3b0;
    --photo-cool: #a9b4d8;
    --photo-red: #e8202a;
  }
  * { box-sizing: border-box; margin: 0; padding: 0; }
  html, body {
    width: 1200px;
    height: 1200px;
    overflow: hidden;
    background: var(--page-bg);
  }
  .canvas {
    width: 1200px;
    height: 1200px;
    display: flex;
    align-items: center;
    justify-content: center;
  }
  .book-cover {
    position: relative;
    width: 790px;
    height: 1120px;
    background: linear-gradient(180deg, var(--cover-pink) 0%, var(--cover-pink) 60%, var(--cover-pink-deep) 100%);
    overflow: hidden;
  }
  .author-name {
    position: absolute;
    top: 118px;
    left: 0;
    width: 100%;
    text-align: center;
    font-family: "Spectral", Georgia, serif;
    font-weight: 600;
    font-size: 30px;
    color: var(--accent-red);
    letter-spacing: 0.5px;
  }
  .book-title {
    position: absolute;
    top: 190px;
    left: 70px;
    width: 660px;
    font-family: "Gochi Hand", cursive;
    font-weight: 400;
    color: var(--title-white);
    line-height: 0.95;
    text-shadow: 2px 3px 4px rgba(150, 60, 90, 0.25);
  }
  .book-title .line-one {
    display: block;
    font-size: 128px;
    text-align: right;
  }
  .book-title .line-two {
    display: block;
    font-size: 128px;
    padding-left: 70px;
  }
  .cover-photo {
    position: absolute;
    right: 40px;
    top: 420px;
    width: 450px;
    height: 565px;
    border-radius: 200px 200px 0 0;
    background:
      radial-gradient(circle at 48% 50%, var(--photo-red) 0 22%, transparent 23%),
      linear-gradient(180deg, #8a5a45 0%, var(--photo-warm) 28%, var(--photo-cool) 65%, #c9a98c 100%);
  }
  .subtitle-band {
    position: absolute;
    left: 0;
    bottom: 0;
    width: 100%;
    height: 135px;
    background: var(--accent-red);
    display: flex;
    flex-direction: column;
    align-items: center;
    justify-content: center;
    font-family: "Spectral", Georgia, serif;
    font-weight: 500;
    font-size: 27px;
    line-height: 1.45;
    color: var(--subtitle-white);
    text-align: center;
  }
</style>
</head>
<body>
  <main class="canvas">
    <article class="book-cover">
      <p class="author-name">Jana Roth</p>
      <h1 class="book-title">
        <span class="line-one">Innere Ruhe</span>
        <span class="line-two">finden</span>
      </h1>
      <div class="cover-photo" role="img" aria-label="Foto einer lächelnden jungen Frau mit langen braunen Haaren in einem geblümten Kleid, die ein großes rotes Herz an sich drückt"></div>
      <div class="subtitle-band">
        <p>Wie aus kleinen Gewohnheiten jeden Tag</p>
        <p>neue Gelassenheit im Alltag wächst</p>
      </div>
    </article>
  </main>
</body>
</html>
```